A Label for an ECO Friendly Spirit Company

Design a label which can be used for vodka and gin (London Dry Gin). It should be Square type Like the Shape File you see in the uploads. VORK means Local Eco friendly Authentic and Fair. We want a cool and slim label that calls for eco-friendly. We want to use it for our premium
Vodka and our London Dry Gin. Please use the logo and design it in Square Type.

40%vol, 700ml

Target Market(s)

spirits and events

Industry/Entity Type

SPIRITS

Colors
00AB8E
00BBA5
67D7C9
C6EFE9
E9F9F6
59FF00
82FF00
B8FF75
E3FFCB
F4FFEA

Requirements
Must have
• Logo from VORK, Squaee Shape

```html
<!DOCTYPE html>
<html lang="en">
<head>
<meta charset="utf-8">
<title>VORK Vodka &amp; Gin Label</title>
<link rel="stylesheet" href="https://fonts.googleapis.com/css2?family=Montserrat:wght@600&family=Oswald:wght@400;500;600&display=swap">
<style>
  :root {
    --bg: #000000;
    --label-black: #000000;
    --gold: #BC9A4C;
    --gold-muted: #8E7538;
    --teal: #00AB8E;
    --lime: #8CC63F;
  }
  html, body {
    margin: 0;
    padding: 0;
    width: 1200px;
    height: 1200px;
    overflow: hidden;
    background: var(--bg);
  }
  .canvas {
    position: relative;
    width: 1200px;
    height: 1200px;
    background: var(--bg);
  }
  .label {
    position: absolute;
    left: 140px;
    top: 140px;
    width: 920px;
    height: 920px;
    display: block;
  }
  .label-frame { fill: var(--label-black); stroke: var(--gold); stroke-width: 14; }
  .diamond-outer { fill: none; stroke: var(--teal); stroke-width: 6; }
  .diamond-inner { fill: none; stroke: var(--gold); stroke-width: 6; }
  .rule { stroke: var(--gold); stroke-width: 2; }
  .ornament { fill: var(--gold-muted); }
  .brand-dot { fill: var(--lime); }
  .brand-name {
    font-family: "Montserrat", sans-serif;
    font-weight: 600;
    font-size: 196px;
    fill: var(--teal);
  }
  .product-type {
    font-family: "Oswald", sans-serif;
    font-weight: 600;
    font-size: 66px;
    fill: var(--gold);
  }
  .figure {
    font-family: "Oswald", sans-serif;
    font-weight: 600;
    font-size: 106px;
    fill: var(--gold);
  }
  .unit {
    font-family: "Oswald", sans-serif;
    font-weight: 400;
    font-size: 40px;
    fill: var(--gold);
  }
</style>
</head>
<body>
<main class="canvas">
  <svg class="label" viewBox="125 432 1068 1068" role="img" aria-label="VORK Vodka and Gin square label, 40% vol, 700 ml">
    <!-- frame -->
    <rect class="label-frame" x="132" y="439" width="1054" height="1054" rx="78" ry="78"/>

    <!-- ornament areas, kept clear of the diamond -->
    <path class="ornament" role="img" aria-label="Gold floral flourish, top left corner"
          d="M215,515 H455 Q470,515 460,528 L200,788 Q185,800 185,780 V545 Q185,515 215,515 Z"/>
    <path class="ornament" role="img" aria-label="Gold floral flourish, top right corner"
          d="M1103,515 H863 Q848,515 858,528 L1118,788 Q1133,800 1133,780 V545 Q1133,515 1103,515 Z"/>
    <path class="ornament" role="img" aria-label="Gold floral flourish, top of diamond"
          d="M659,515 L748,598 Q752,604 744,604 H574 Q566,604 570,598 Z"/>
    <path class="ornament" role="img" aria-label="Gold floral flourish, bottom of diamond"
          d="M659,1418 L748,1335 Q752,1329 744,1329 H574 Q566,1329 570,1335 Z"/>

    <!-- diamond -->
    <polygon class="diamond-outer" points="659,436 1190,966 659,1496 128,966"/>
    <polygon class="diamond-inner" points="659,452 1173,966 659,1480 145,966"/>

    <!-- brand -->
    <circle class="brand-dot" cx="659" cy="760" r="100"/>
    <line class="rule" x1="312" y1="878" x2="557" y2="878"/>
    <line class="rule" x1="793" y1="878" x2="1006" y2="878"/>
    <text class="brand-name" x="659" y="1085" text-anchor="middle">VORK</text>

    <line class="rule" x1="415" y1="1118" x2="903" y2="1118"/>
    <text class="product-type" x="441" y="1192" textLength="441" lengthAdjust="spacing">VODKA &amp; GIN</text>
    <line class="rule" x1="415" y1="1214" x2="903" y2="1214"/>

    <!-- strength -->
    <text class="figure" x="174" y="1403">40</text>
    <text class="unit" x="308" y="1345">%</text>
    <text class="unit" x="300" y="1403">VOL</text>

    <!-- volume -->
    <text class="figure" x="934" y="1403">700</text>
    <text class="unit" x="1106" y="1403">ML</text>
  </svg>
</main>
</body>
</html>
```